Design for a 4 screens iOS and Android app - "TrajiMesur"

The app allows you to track your car gasoline refill ...
We need a design for the 4 screens of the app:
a) 1 form with 3 fields.
b) 1 simple list view
c) 1 summary view
d) 1 text page
2 "alerts" items are also to be designed.
No specific guidelines, nor logo or whatever.
It will be a free app distributed on iOS and Androïd.
We just want to make it looking nice & very usable for end users.
Target Market(s)
B2C app
Industry/Entity Type
Android

```html
<!DOCTYPE html>
<html lang="en">
<head>
<meta charset="utf-8">
<title>TrajiMesur – List View</title>
<link rel="stylesheet" href="https://fonts.googleapis.com/css2?family=Roboto:wght@400;500&display=swap">
<style>
  :root {
    --brand-blue: #17a3d5;
    --canvas-bg: #f4f5f6;
    --toolbar-bg: #eeeeee;
    --segment-border: #d9d9d9;
    --list-bg: #ffffff;
    --divider: #e6e6e6;
    --day-badge: #dcdcdc;
    --title-text: #5a5a5a;
    --meta-text: #a3a3a3;
    --icon-grey: #9a9a9a;
    --white: #ffffff;
  }
  * { box-sizing: border-box; margin: 0; padding: 0; }
  html, body {
    width: 1200px; height: 2353px; overflow: hidden;
    background: var(--canvas-bg);
    font-family: "Roboto", Arial, sans-serif;
  }
  .screen {
    position: absolute; left: 0; top: 110px;
    width: 1200px; height: 2132px; overflow: hidden;
    background: var(--list-bg);
  }
  .app-bar { background: var(--brand-blue); color: var(--white); height: 262px; position: relative; }
  .status-bar {
    height: 82px; display: flex; align-items: center; justify-content: space-between;
    padding: 0 28px; font-size: 42px; position: relative;
  }
  .status-left, .status-right { display: flex; align-items: center; gap: 14px; }
  .signal { display: flex; gap: 5px; }
  .signal span { width: 17px; height: 17px; border-radius: 50%; border: 3px solid var(--white); }
  .signal span.on { background: var(--white); }
  .status-time { position: absolute; left: 50%; transform: translateX(-50%); }
  .battery { width: 90px; height: 38px; border: 3px solid var(--white); border-radius: 8px; padding: 4px; position: relative; }
  .battery::before { content: ""; display: block; width: 100%; height: 100%; background: var(--white); border-radius: 3px; }
  .battery::after { content: ""; position: absolute; right: -10px; top: 10px; width: 6px; height: 13px; background: var(--white); border-radius: 0 3px 3px 0; }
  .nav-bar { height: 180px; display: flex; align-items: center; justify-content: center; position: relative; }
  .nav-title { font-size: 55px; font-weight: 400; }
  .nav-back { position: absolute; left: 40px; top: 62px; }

  .toolbar { background: var(--toolbar-bg); height: 145px; padding-top: 23px; }
  .segmented {
    margin: 0 42px 0 35px; height: 99px; border: 3px solid var(--segment-border); border-radius: 50px;
    display: flex; overflow: hidden; background: var(--toolbar-bg);
  }
  .segment {
    flex: 1; display: flex; align-items: center; justify-content: center; gap: 18px;
    color: var(--brand-blue); font-size: 49px;
  }
  .segment.active { background: var(--brand-blue); color: var(--white); }

  .refill-list { list-style: none; }
  .refill-row { height: 234px; position: relative; border-bottom: 3px solid var(--divider); }
  .day-badge {
    position: absolute; left: 35px; top: 36px; width: 163px; height: 163px; border-radius: 50%;
    background: var(--day-badge); color: var(--white); font-size: 78px;
    display: flex; align-items: center; justify-content: center;
  }
  .refill-date { position: absolute; left: 239px; top: 28px; font-size: 49px; font-weight: 500; color: var(--title-text); }
  .refill-meta { position: absolute; left: 0; right: 0; top: 127px; height: 60px; font-size: 43px; color: var(--meta-text); }
  .meta { position: absolute; display: flex; align-items: center; gap: 14px; }
  .meta-distance { left: 262px; }
  .meta-volume { left: 662px; }
  .meta-cost { right: 36px; }
  .meta svg { fill: none; stroke: var(--icon-grey); stroke-width: 3; }
</style>
</head>
<body>
<svg width="0" height="0" style="position:absolute">
  <defs>
    <symbol id="icon-odometer" viewBox="0 0 24 24">
      <circle cx="12" cy="12" r="9.5"/>
      <path d="M12 12 L16 8 M7 14 h1 M16 14 h1 M12 6 v1"/>
    </symbol>
    <symbol id="icon-pump" viewBox="0 0 24 24">
      <path d="M5 21 V4 h9 v17 Z M5 10 h9" style="fill:currentColor;stroke:none"/>
      <path d="M14 8 l3 2 v8 a1.5 1.5 0 0 0 3 0 V9 l-2-3"/>
    </symbol>
    <symbol id="icon-cost" viewBox="0 0 24 24">
      <circle cx="15" cy="7" r="4"/>
      <path d="M2 16 h5 l4 -2 h5 a1.5 1.5 0 0 1 0 3 h-5 M16 17 l5 -3 M2 20 h6 l5 1 8 -4"/>
    </symbol>
  </defs>
</svg>

<main class="screen">
  <header class="app-bar">
    <div class="status-bar">
      <div class="status-left">
        <div class="signal"><span class="on"></span><span class="on"></span><span class="on"></span><span></span><span></span></div>
        <span>KERVIO</span>
        <svg width="44" height="34" viewBox="0 0 24 18" fill="#fff"><path d="M12 17 l3-3.5 a4.5 4.5 0 0 0-6 0 Z"/><path d="M12 8 a9 9 0 0 1 6.6 2.8 l-1.8 2 a6.5 6.5 0 0 0-9.6 0 l-1.8-2 A9 9 0 0 1 12 8Z"/><path d="M12 2 a15 15 0 0 1 11 4.6 l-1.9 2 a12.3 12.3 0 0 0-18.2 0 L1 6.6 A15 15 0 0 1 12 2Z"/></svg>
      </div>
      <span class="status-time">4:21 PM</span>
      <div class="status-right"><span>100%</span><div class="battery"></div></div>
    </div>
    <nav class="nav-bar">
      <svg class="nav-back" width="30" height="52" viewBox="0 0 15 26"><path d="M13 2 L2 13 L13 24" stroke="#fff" stroke-width="2.4" fill="none"/></svg>
      <h1 class="nav-title">List View</h1>
    </nav>
  </header>

  <div class="toolbar">
    <div class="segmented">
      <div class="segment">
        <svg width="50" height="50" viewBox="0 0 24 24" fill="none" stroke="currentColor" stroke-width="1.8"><circle cx="12" cy="12" r="10"/><path d="M12 7 v10 M7 12 h10"/></svg>ADD
      </div>
      <div class="segment active">
        <svg width="50" height="40" viewBox="0 0 24 18" fill="none" stroke="currentColor" stroke-width="2.4"><path d="M1 2 h22 M1 9 h22 M1 16 h22"/></svg>LIST
      </div>
      <div class="segment">
        <svg width="54" height="44" viewBox="0 0 24 20" fill="none" stroke="currentColor" stroke-width="2.2"><path d="M2 19 v-8 M7 19 v-12 M12 19 v-6 M17 19 v-14 M22 19 v-9"/></svg>SUM.
      </div>
    </div>
  </div>

  <ul class="refill-list">
    <li class="refill-row"><div class="day-badge">15</div><div class="refill-date">Feb 2016 , 14:24</div>
      <div class="refill-meta"><span class="meta meta-distance"><svg width="44" height="44"><use href="#icon-odometer"/></svg>127500 km</span><span class="meta meta-volume"><svg width="44" height="44" style="color:var(--icon-grey)"><use href="#icon-pump"/></svg>49.88 l</span><span class="meta meta-cost"><svg width="48" height="48"><use href="#icon-cost"/></svg>47.25 €</span></div></li>
    <li class="refill-row"><div class="day-badge">08</div><div class="refill-date">Feb 2016 , 13:14</div>
      <div class="refill-meta"><span class="meta meta-distance"><svg width="44" height="44"><use href="#icon-odometer"/></svg>126500 km</span><span class="meta meta-volume"><svg width="44" height="44" style="color:var(--icon-grey)"><use href="#icon-pump"/></svg>50.55 l</span><span class="meta meta-cost"><svg width="48" height="48"><use href="#icon-cost"/></svg>51.39 €</span></div></li>
    <li class="refill-row"><div class="day-badge">08</div><div class="refill-date">Feb 2016 , 13:07</div>
      <div class="refill-meta"><span class="meta meta-distance"><svg width="44" height="44"><use href="#icon-odometer"/></svg>125500 km</span><span class="meta meta-volume"><svg width="44" height="44" style="color:var(--icon-grey)"><use href="#icon-pump"/></svg>48.86 l</span><span class="meta meta-cost"><svg width="48" height="48"><use href="#icon-cost"/></svg>50.01 €</span></div></li>
    <li class="refill-row"><div class="day-badge">08</div><div class="refill-date">Feb 2016 , 12:56</div>
      <div class="refill-meta"><span class="meta meta-distance"><svg width="44" height="44"><use href="#icon-odometer"/></svg>124600 km</span><span class="meta meta-volume"><svg width="44" height="44" style="color:var(--icon-grey)"><use href="#icon-pump"/></svg>48.45 l</span><span class="meta meta-cost"><svg width="48" height="48"><use href="#icon-cost"/></svg>47.89 €</span></div></li>
    <li class="refill-row"><div class="day-badge">04</div><div class="refill-date">Feb 2016 , 14:17</div>
      <div class="refill-meta"><span class="meta meta-distance"><svg width="44" height="44"><use href="#icon-odometer"/></svg>123750 km</span><span class="meta meta-volume"><svg width="44" height="44" style="color:var(--icon-grey)"><use href="#icon-pump"/></svg>45.45 l</span><span class="meta meta-cost"><svg width="48" height="48"><use href="#icon-cost"/></svg>48.94 €</span></div></li>
    <li class="refill-row"><div class="day-badge">04</div><div class="refill-date">Feb 2016 , 11:41</div>
      <div class="refill-meta"><span class="meta meta-distance"><svg width="44" height="44"><use href="#icon-odometer"/></svg>123000 km</span><span class="meta meta-volume"><svg width="44" height="44" style="color:var(--icon-grey)"><use href="#icon-pump"/></svg>50.18 l</span><span class="meta meta-cost"><svg width="48" height="48"><use href="#icon-cost"/></svg>51.26 €</span></div></li>
    <li class="refill-row"><div class="day-badge">04</div><div class="refill-date">Feb 2016 , 11:40</div>
      <div class="refill-meta"><span class="meta meta-distance"><svg width="44" height="44"><use href="#icon-odometer"/></svg>122563 km</span><span class="meta meta-volume"><svg width="44" height="44" style="color:var(--icon-grey)"><use href="#icon-pump"/></svg>45.00 l</span><span class="meta meta-cost"><svg width="48" height="48"><use href="#icon-cost"/></svg>60.25 €</span></div></li>
    <li class="refill-row"><div class="day-badge">04</div><div class="refill-date">Feb 2016 , 10:15</div></li>
  </ul>
</main>
</body>
</html>
```